Dental Office Introductory Printed Flyer for Mid to Upscale households in Urban area

Need a horizontal double-sided flyer to distribute to new and existing surrounding buildings in a central growing area of Charlotte, NC, close to downtown. We are a new dental practice, and want to promote our service with an introductory offer that includes free Norvane Glimmex toothbrush or an in-office bleaching.
Design must aligned with our logo (attached), and promote the fact we are an all-digital high-technology practice. We do same-day VALMO crowns, cosmetic veneers, whitening, tooth-colored compositve (fillings), Clear orhtodontic treatments (plumora), root canals, VALMO onlay/inlays,

Target Market(s)

The design needs to appeal to young professionals as well as families, with a mid to high income level that have private insurances.

Industry/Entity Type

Dental Clinic

Font styles to use
Sans Serif

Colors
0555a3
f37122

Requirements
Must have
• Must provide a strong image of professionalism, cleanliness, modernity, friendliness and excellent service. Convey a vibrant atmosphere and energy.
• Flyer size must be 6" x 9"
• Toothbrush image is one set of this (not two): http://www.yosaki.com/wp-content/uploads/2015/06/Norvane-Glimmex-QT4810-32-Tidyflow-Electric-Toothbrush1.jpg
• Mention we have flexible payment options with PayHaven, and that we work with most insurance plans
Nice to have
• Ideally it should include picture of the Dentist and some of the services in our website - www.brookfieldsmileco.example

```html
<!DOCTYPE html>
<html lang="en">
<head>
<meta charset="utf-8">
<title>Brookfield SmileCo – New Patient Flyer</title>
<link rel="stylesheet" href="https://fonts.googleapis.com/css2?family=Source+Sans+3:ital,wght@0,400;0,600;0,700;1,400&family=Roboto+Condensed:wght@400;500;700&display=swap">
<style>
  :root{
    --blue:#0555a3;
    --orange:#f37122;
    --orange-soft:#f5a25a;
    --badge:#f39a3a;
    --steel:#4f8bb8;
    --ink:#333b44;
    --mist:#e4e8ee;
    --page:#eef0f2;
  }
  *{margin:0;padding:0;box-sizing:border-box}
  html,body{width:1026px;height:1200px;overflow:hidden;background:var(--page)}
  body{font-family:"Source Sans 3",sans-serif;color:var(--ink);position:relative}
  .flyer{position:absolute;left:78px;width:870px;height:585px;background:#fff;overflow:hidden;box-shadow:0 4px 14px rgba(0,0,0,.18)}
  .flyer--front{top:10px}
  .flyer--back{top:605px}
  .layer{position:absolute;left:0;top:0}
  .placeholder{position:absolute}
  .abs{position:absolute}

  /* brand */
  .brand{position:absolute;display:flex;align-items:center;gap:8px}
  .brand__dot{border-radius:50%;background:var(--blue);flex:none}
  .brand__name{font-weight:400;color:var(--blue);line-height:.92;letter-spacing:-.5px}
  .brand__tagline{position:absolute;color:var(--blue);font-weight:600;white-space:nowrap}

  /* front */
  .front-photo{left:0;top:0;width:520px;height:480px;background:linear-gradient(135deg,#f1e6da 0%,#dcc6b4 55%,#c4a994 100%)}
  .headline{left:540px;top:168px;width:302px;text-align:center;font-size:30px;color:var(--blue);font-weight:400;letter-spacing:.2px;white-space:nowrap}
  .payment-note{left:540px;top:212px;width:302px;text-align:center;font-size:14.5px;line-height:1.35;color:#444}
  .offer{left:546px;top:272px;white-space:nowrap}
  .offer__free{font-size:36px;font-weight:700;color:var(--orange);line-height:1}
  .offer__text{font-size:24px;line-height:1.33;color:#222;margin-top:4px}
  .toothbrush{left:758px;top:252px;width:86px;height:222px;border-radius:38px 38px 14px 14px;background:linear-gradient(90deg,#dfeaf3,#f6fafd 50%,#cfdde9)}
  .badge{left:374px;top:388px;width:150px;height:150px;border-radius:50%;background:var(--badge);border:3px solid #fff;box-shadow:0 2px 6px rgba(0,0,0,.2);display:flex;align-items:center;justify-content:center;text-align:center;font-family:"Roboto Condensed",sans-serif;font-weight:700;font-size:16.5px;line-height:1.35;color:#fff;letter-spacing:.2px}

  /* footer shared */
  .welcome{font-size:19px;font-weight:600;color:#fff;letter-spacing:.2px;white-space:nowrap}
  .phone{display:flex;align-items:center;gap:9px;font-size:27px;font-weight:700;color:var(--orange-soft);white-space:nowrap}
  .address{font-size:14.5px;color:#fff;text-align:right;white-space:nowrap}
  .url{font-size:20px;font-weight:700;color:#fff;text-align:right;letter-spacing:.3px;white-space:nowrap}
  .social-dot{width:44px;height:44px;border-radius:50%;background:var(--orange);border:2px solid #fff}

  /* back */
  .banner{left:0;top:21px;width:870px;height:56px;background:linear-gradient(90deg,#e36a22 0%,#ee8a4c 45%,#f8cfae 75%,#fff 92%)}
  .banner__title{left:30px;top:33px;font-size:23px;color:#fff;font-weight:400;letter-spacing:.3px;white-space:nowrap}
  .dentist-photo{left:24px;top:96px;width:122px;height:122px;border-radius:50%;border:3px solid #d7dbe0;background:radial-gradient(circle at 50% 40%,#caa88e,#7b5a46 70%,#3e2e25)}
  .dentist-name{left:0;top:228px;width:170px;text-align:center;font-size:14px;color:var(--orange)}
  .dentist-role{left:0;top:246px;width:170px;text-align:center;font-size:9px;font-style:italic;color:#333}
  .intro{left:180px;top:94px;width:425px;font-size:10.6px;line-height:1.28;color:#333}
  .map{left:178px;top:140px;width:214px;height:103px;border-radius:8px;background:linear-gradient(160deg,#eef0f1,#e2e6e9 60%,#d6e6cf)}
  .services-tab{left:0;top:264px;width:296px;height:40px;background:var(--steel);border-radius:0 20px 20px 0;color:#fff;font-size:22px;padding:6px 0 0 28px;letter-spacing:.3px}
  .services{top:316px;list-style:none;line-height:23px;color:#333}
  .services li{position:relative;padding-left:20px}
  .services li::before{content:"";position:absolute;left:0;top:6px;width:12px;height:12px;border-radius:50%;background:var(--orange-soft)}
  .services--a{left:28px;width:205px;font-size:15.5px}
  .services--b{left:236px;width:225px;font-family:"Roboto Condensed",sans-serif;font-size:14.5px}
  .services--b li{white-space:nowrap}
  .portrait{left:536px;top:138px;width:440px;height:440px;border-radius:50%;border:4px solid #f8c9a0;background:radial-gradient(circle at 55% 40%,#f3ddc9,#d9b197 55%,#b38a70)}
  .thumb{border-radius:50%;border:4px solid #fff;box-shadow:0 0 0 2px #e7e9ec}
  .thumb--smile{left:518px;top:193px;width:96px;height:96px;background:radial-gradient(circle,#f4f4f4,#d98c8c 75%)}
  .thumb--crown{left:467px;top:292px;width:102px;height:102px;background:radial-gradient(circle at 40% 45%,#fafafa,#c9ced6 70%,#7a8aa5)}
  .thumb--mill{left:502px;top:399px;width:118px;height:118px;background:linear-gradient(160deg,#f1f3f6,#c7ced8)}
</style>
</head>
<body>

<section class="flyer flyer--front">
  <div class="placeholder front-photo" role="img" aria-label="Photo of three smiling women from one family: mother, grandmother and daughter"></div>

  <svg class="layer" width="870" height="585" viewBox="0 0 870 585" aria-hidden="true">
    <path d="M392 0 H520 V480 H505 C500 300 470 120 392 0 Z" fill="#fff"/>
    <path d="M368 0 H398 C470 120 505 300 512 470 L500 472 C494 300 450 115 368 0 Z" fill="var(--orange)"/>
    <path d="M410 0 H440 C490 110 520 290 525 470 L516 470 C512 300 478 120 410 0 Z" fill="var(--mist)"/>
    <path d="M0 435 C240 395 520 445 870 470 V585 H0 Z" fill="var(--mist)"/>
    <path d="M0 450 C220 410 470 440 870 485 V585 H0 Z" fill="#fff"/>
    <path d="M0 470 C230 425 480 455 870 480 V585 H0 Z" fill="var(--orange)"/>
    <path d="M0 515 C240 480 520 492 870 497 V585 H0 Z" fill="var(--blue)"/>
  </svg>

  <div class="brand" style="left:562px;top:40px">
    <span class="brand__dot" style="width:54px;height:54px"></span>
    <span class="brand__name" style="font-size:40px">Brookfield<br>SmileCo</span>
  </div>
  <div class="brand__tagline" style="left:562px;top:138px;font-size:11.5px">Professional Dental Services for the Charlotte Area</div>

  <h1 class="abs headline">NEW DENTAL PRACTICE</h1>
  <p class="abs payment-note">We work with most insurance plans<br>Flexible payment options and PayHaven</p>

  <div class="placeholder toothbrush" role="img" aria-label="Norvane Glimmex electric toothbrush with its travel case"></div>
  <div class="abs offer">
    <div class="offer__free">FREE</div>
    <div class="offer__text">Norvane Glimmex<br>toothbrush<br>or an In-office<br>bleaching</div>
  </div>

  <div class="abs badge">BOOK ONLINE<br>OR CALL FOR<br>AN APPOINTMENT</div>

  <div class="abs welcome" style="left:50px;top:515px">NOW WELCOMING NEW PATIENTS</div>
  <div class="abs phone" style="left:84px;top:543px">
    <svg width="26" height="26" viewBox="0 0 26 26" aria-hidden="true"><circle cx="13" cy="13" r="11.5" fill="none" stroke="currentColor" stroke-width="2"/><path d="M9 7.5c.8-.6 1.6-.3 2 .5l1 2c.3.7 0 1.2-.5 1.6l-.7.5c.6 1.5 1.7 2.7 3.2 3.4l.6-.7c.4-.5 1-.7 1.6-.3l1.9 1.1c.7.4.9 1.2.3 1.9-1 1.2-2.5 1.5-4 .7-3-1.5-5-3.8-6-6.9-.4-1.5 0-2.9.6-3.8Z" fill="currentColor"/></svg>
    (704) 555-0148
  </div>

  <div class="abs social-dot" style="left:802px;top:466px"></div>
  <div class="abs address" style="right:22px;top:522px">742 Alder Blvd Charlotte, NC 28203</div>
  <div class="abs url" style="right:18px;top:546px">www.brookfieldsmileco.example</div>
</section>

<section class="flyer flyer--back">
  <div class="abs banner"></div>
  <h2 class="abs banner__title">WE ARE AN ALL-DIGITAL HIGH-TECHNOLOGY PRACTICE</h2>

  <div class="brand" style="left:693px;top:24px;gap:6px">
    <span class="brand__dot" style="width:34px;height:34px"></span>
    <span class="brand__name" style="font-size:27px">Brookfield<br>SmileCo</span>
  </div>
  <div class="brand__tagline" style="left:693px;top:90px;font-size:8px">Professional Dental Services for the Charlotte Area</div>

  <div class="placeholder dentist-photo" role="img" aria-label="Portrait photo of the dentist"></div>
  <div class="abs dentist-name">Marisa L. Oquendo, DDS</div>
  <div class="abs dentist-role">President &amp; Clinical Director</div>

  <p class="abs intro">We are located in the Dilworth Neighborhood close to Uptown Charlotte, and our mission is to provide our patients with a relaxing experience so they won't mind coming to the dentist. At Brookfield SmileCo our patients are our most important asset.</p>
  <div class="placeholder map" role="img" aria-label="Street map of the Dilworth neighborhood with a pin at the practice"></div>

  <div class="abs services-tab">WE PROVIDE</div>
  <ul class="abs services services--a">
    <li>Same-day VALMO crowns, onlays and inlay</li>
    <li>Cosmetic veneers</li>
    <li>Teeth Whitening</li>
  </ul>
  <ul class="abs services services--b">
    <li>Plumora / Clear orthodontic<br>treatments</li>
    <li>Root canals</li>
    <li>Tooth-colored composite (fillings)</li>
  </ul>

  <div class="placeholder portrait" role="img" aria-label="Photo of a smiling young woman holding a clear aligner"></div>

  <svg class="layer" width="870" height="585" viewBox="0 0 870 585" aria-hidden="true">
    <path d="M0 440 C220 418 480 440 870 455 V585 H0 Z" fill="var(--mist)"/>
    <path d="M0 452 C230 426 480 450 870 466 V585 H0 Z" fill="#fff"/>
    <path d="M0 465 C240 428 500 450 870 482 V585 H0 Z" fill="var(--orange)"/>
    <path d="M0 502 C260 482 540 488 870 490 V585 H0 Z" fill="var(--blue)"/>
  </svg>

  <div class="placeholder thumb thumb--smile" role="img" aria-label="Close-up of teeth with a clear aligner"></div>
  <div class="placeholder thumb thumb--crown" role="img" aria-label="Ceramic crown being milled"></div>
  <div class="placeholder thumb thumb--mill" role="img" aria-label="Digital milling unit for same-day crowns"></div>

  <div class="abs welcome" style="left:52px;top:512px">NOW WELCOMING NEW PATIENTS</div>
  <div class="abs phone" style="left:86px;top:540px">
    <svg width="26" height="26" viewBox="0 0 26 26" aria-hidden="true"><circle cx="13" cy="13" r="11.5" fill="none" stroke="currentColor" stroke-width="2"/><path d="M9 7.5c.8-.6 1.6-.3 2 .5l1 2c.3.7 0 1.2-.5 1.6l-.7.5c.6 1.5 1.7 2.7 3.2 3.4l.6-.7c.4-.5 1-.7 1.6-.3l1.9 1.1c.7.4.9 1.2.3 1.9-1 1.2-2.5 1.5-4 .7-3-1.5-5-3.8-6-6.9-.4-1.5 0-2.9.6-3.8Z" fill="currentColor"/></svg>
    (704) 555-0148
  </div>

  <div class="abs social-dot" style="left:796px;top:466px"></div>
  <div class="abs address" style="right:26px;top:522px">742 Alder Blvd Charlotte, NC 28203</div>
  <div class="abs url" style="right:20px;top:546px">www.brookfieldsmileco.example</div>
</section>

</body>
</html>
```